Small Business Directory Site Requires a Professional Responsive Web Design

Small Business Directory and Coupon Site - we require a complete website design for a brand new responsive & mobile friendly website. We already have a coder who will professional code our website in Magento.

All PSD pages need to be professionally designed then uploaded into a sharedrive (i.e. like dropbox). Additionally, as I cannot pre-empt everything, please note that we may require a little more assistance once the files have been transferred (for example, in www.brindlestack.com if you hover your mouse on the search box you will see a pop up box. We want one of these too and I think that means there may be extra design work here)

We have some draft page sketches have been created (there are some minor changes we want to the sketches provided though); however, we require an excellent designer to add the creative touches to it to make it look professionally created. All artwork/font must be legal.

-------------------------
We like the look of the www.brindlestack.com and www. quorvanet.com

For the headers, please consider a font similar to RNS camellia. We likes this style, but it is too thin for the headers...so we need a variation like this one. For the copy/general text font, something basic that marries well with the headers.

---------------------

Please be sure to also read the brief we wrote for the coder as this will help with better understanding our design requirements.

In total I believe we have about 50 pages. This includes all the little pages and most of the pop up boxes (but not the little help key boxes). For example, pages include...

1. Login (this is where customers log in and can edit, manage their profiles. This means that there are backend membership pages)
2. Mini Services (same look and feel as the business coupons)
3. Resource Centre
4. Join (this is where customers learn about the packages available to submit a directory listing, if they ‘buy’ a package (i.e. free, $25 or $150 package) then they can create their own directory listing)
5. Search the directory (customer can view all the categories and also search the directory)
6. Create a directory listing (this is where customers learn about the packages available to submit a directory listing, if they ‘buy’ a package (i.e. free, $25 or $150 package) then they can create their own directory listing)
7. Quote finder (also know as Get a Quote)
8. Coupons (customer go to the business coupon page and can view all current coupons/submit a coupon)
9. Submit a coupon (form)
10.Advertise with us (form)
11. Join the forum
12.Submit an article or video (form)
13. Affiliates (listing of affiliates we currently have)
14. Become an affiliate (form)
15. Case studies (customer can view the case studies we have in the resource centre)
16. Help Guides (customer can view the help guides we have in the resource centre)
17. About Us
18 .Contact Us (form)
19. Terms & Condition
20. Privacy Policy
21. Supporting City Councils
22. Site Map
23. Forgot password / login details
24. Homepage
25. If we hover over a few areas (i.e. search box, location field) it pops up with more information.
etc etc etc. . . there are more pages.

Please see our dropbox link for the draft mock up pages that I have created so far.

https://www.filmorrow.com/sh/kq82pl4vmd7wtz/QZtrXnBeLopVacd3Ju7fGhWkS

We are in a rush! We'd like to get the majority of the artwork completed by the end of the month. Minor fixes/tweaks can occur thereafter.

Target Market(s)

Small Businesses (employees 0 - 50) located throughout Australia

Industry/Entity Type

Business

Font styles to use
Sans Serif

Requirements
Must have
• Professional. Artwork must be legal (cannot be cut and paste or taken off other websites, must be legally purchased and used).Must look contemporary, fresh, modern.

Absolutely must be a responsive site!
Nice to have
• original work, original photos, original art.

like modern, fresh photos that demonstrate innovation, growth, small business, Australian scenery, stability, goals/passion.
Should not have
• cut and paste graphics, illegal graphics, not purchased graphics.

```html
<!DOCTYPE html>
<html lang="en">
<head>
<meta charset="utf-8">
<title>Tallyroo Link – Australia's Small Business Support Link</title>
<link rel="stylesheet" href="https://fonts.googleapis.com/css2?family=Open+Sans:wght@400;600;700&family=Questrial&family=Tinos:wght@400;700&display=swap">
<style>
:root{
  --black:#0d0d0d;
  --orange:#f7860f;
  --orange-dark:#e07406;
  --teal:#2a8fae;
  --brown:#3a2f27;
  --light:#efefef;
  --light-band:#e2e2e2;
  --dark:#232323;
  --footer:#1b1b1b;
  --bottom:#101010;
  --text:#555;
  --muted:#8a8a8a;
  --white:#fff;
}
*{margin:0;padding:0;box-sizing:border-box}
html,body{width:1200px;height:2932px;overflow:hidden}
body{position:relative;font-family:"Open Sans",Arial,sans-serif;font-size:13px;color:var(--text);background:var(--white)}
.abs{position:absolute}
a{color:inherit;text-decoration:none}

/* header */
.site-header{left:0;top:0;width:1200px;height:102px;background:var(--black)}
.brand{left:111px;top:30px;display:flex;align-items:center;gap:12px;color:var(--white);font-size:27px;font-weight:600}
.brand-mark{width:40px;height:40px;background:var(--orange)}
.top-nav{left:440px;top:0;height:39px;display:flex}
.top-nav .links{background:var(--white);display:flex;align-items:center;padding:0 10px;font-size:12.5px;font-weight:700;color:#222;width:533px;justify-content:space-between}
.top-nav .links span.sep{color:#999;font-weight:400}
.top-nav .account{background:var(--orange);color:var(--white);width:117px;display:flex;align-items:center;justify-content:center;font-size:12.5px;font-weight:700;gap:8px}
.social-top{left:965px;top:55px;display:flex;gap:7px}
.sq{width:25px;height:25px;display:block}

/* hero */
.hero{left:0;top:102px;width:1200px;height:572px;background:radial-gradient(ellipse at 50% 35%,#f4e6d2 0%,#dcc3a1 40%,#b9946b 75%,#8c6a48 100%)}
.hero-title{left:111px;top:278px;font-family:"Tinos",serif;font-size:37px;color:#1d1d1d}
.hero-sub{left:111px;top:318px;font-family:"Tinos",serif;font-size:29px;color:#1d1d1d}
.hero-copy{left:111px;top:365px;width:600px;font-size:13.5px;line-height:21px;color:#4a3b2d}
.search{left:111px;top:424px;width:602px;height:76px;background:rgba(255,255,255,.45);border-radius:4px}
.search .field{position:absolute;top:20px;height:35px;background:var(--white);font-size:13px;color:#444;padding:9px 10px}
.search .go{position:absolute;left:463px;top:20px;width:108px;height:35px;background:var(--orange);color:var(--white);font-weight:700;font-size:17px;text-align:center;line-height:35px}
.listing-card{left:817px;top:203px;width:273px;height:358px;background:rgba(90,82,76,.8);border-radius:4px}
.listing-card h3{position:absolute;left:0;top:12px;width:273px;text-align:center;font-family:"Tinos",serif;font-weight:400;font-size:23px;line-height:29px;color:var(--white)}
.listing-inner{position:absolute;left:29px;top:90px;width:213px;height:237px;background:#fbecd6;border:5px solid var(--orange)}
.price-band{position:absolute;left:25px;top:102px;width:222px;height:29px;background:#1f1f1f;color:var(--white);font-family:"Tinos",serif;font-size:17px;text-align:center;line-height:29px}
.listing-inner .cat{position:absolute;top:48px;width:100%;text-align:center;font-family:"Tinos",serif;font-weight:700;font-size:14px;color:#222}
.listing-inner p{position:absolute;top:76px;left:8px;right:8px;text-align:center;font-size:12px;line-height:17px;color:#333}
.listing-inner .go{position:absolute;left:48px;top:170px;width:107px;height:36px;background:#1f1f1f;color:var(--white);font-weight:700;font-size:16px;text-align:center;line-height:36px}
.arrow{position:absolute;color:rgba(255,255,255,.6);font-size:30px;font-family:"Questrial",sans-serif}

/* category bar */
.cat-bar{left:0;top:674px;width:1200px;height:55px;background:var(--brown);display:flex;align-items:center;justify-content:space-between;padding:0 80px 0 111px;color:var(--white);font-size:11.5px;font-weight:600}
.cat-bar span{display:flex;align-items:center;gap:8px}
.cat-bar i{width:16px;height:16px;background:#e8e1da;border-radius:3px;display:block}

/* sections */
.section-light{left:0;width:1200px;background:var(--light)}
.section-title{left:0;width:1200px;text-align:center;font-family:"Questrial",sans-serif;font-size:37px;color:#2a2a2a}
.section-copy{left:152px;width:896px;text-align:center;font-size:13.5px;line-height:22px;color:#777}
.band{left:0;width:1200px;background:var(--light-band)}
.media{position:absolute;border:1px solid #cfcfcf}
.card-title{font-family:"Tinos",serif;font-size:17px;color:#2a2a2a}
.card-copy{font-size:12.5px;line-height:20px;color:#777}
.read-more{font-size:12px;color:var(--orange);text-decoration:underline}
.partner{display:flex;align-items:center;justify-content:center;gap:10px;background:radial-gradient(circle,#fff 45%,#d9d9d9 100%);font-size:24px;font-weight:600;color:#222}
.partner .dot{width:22px;height:22px;background:#222}
.partner .nav{position:absolute;color:#999;font-size:30px;font-family:"Questrial",sans-serif;top:50%;transform:translateY(-55%)}
.offer-tab{left:774px;top:1329px;width:316px;height:45px;background:var(--teal);color:var(--white);font-family:"Tinos",serif;font-size:17px;text-align:center;line-height:45px}

.section-dark{left:0;top:1374px;width:1200px;height:648px;background:var(--dark)}
.dark-title{color:var(--white)}
.dark-sub{left:0;top:1500px;width:1200px;text-align:center;font-size:15px;color:#8d8d8d}
.block h4{font-size:15px;font-weight:700;color:var(--white);margin-bottom:10px}
.block p{font-size:13.5px;line-height:21px;color:#bdbdbd}
.block .hl{color:var(--orange)}
.btn{display:inline-block;background:var(--orange);color:var(--white);font-size:12px;font-weight:700;height:33px;line-height:33px;padding:0 14px}

/* footer */
.site-footer{left:0;top:2634px;width:1200px;height:248px;background:var(--footer)}
.foot-col h5{font-size:13.5px;font-weight:400;color:var(--orange);margin-bottom:12px}
.foot-col li{list-style:none;font-size:12.5px;line-height:22px;color:#cfcfcf}
.social-foot{display:flex;gap:5px;margin-top:4px}
.bottom-bar{left:0;top:2882px;width:1200px;height:50px;background:var(--bottom);color:#bdbdbd;font-size:12px;text-align:center;line-height:50px}
</style>
</head>
<body>

<header class="site-header abs">
  <div class="brand abs"><span class="brand-mark"></span>Tallyroo Link</div>
  <nav class="top-nav abs">
    <div class="links"><a>COUPONS</a><span class="sep">|</span><a>MINI SERVICES</a><span class="sep">|</span><a>GET A QUOTE</a><span class="sep">|</span><a>ADVERTISE</a><span class="sep">|</span><a>RESOURCE CENTRE</a></div>
    <div class="account"><a>LOGIN</a><span>|</span><a>JOIN</a></div>
  </nav>
  <div class="social-top abs">
    <span class="sq" style="background:#1da1f2"></span>
    <span class="sq" style="background:#f39a2b"></span>
    <span class="sq" style="background:#3b5998"></span>
    <span class="sq" style="background:#e94e8d"></span>
  </div>
</header>

<section class="hero abs" role="img" aria-label="Softly blurred warm office interior with a wooden desk in the foreground"></section>
<h1 class="hero-title abs" style="font-weight:400">Let Us Help You Grow.</h1>
<h2 class="hero-sub abs" style="font-weight:400">Australia's Small Business Support Link</h2>
<p class="hero-copy abs">Lorem ipsum dolor sit amet, consectetur adipiscing elit, sed do eiusmod tempor incididunt ut labore et dolore magna aliqua.</p>
<form class="search abs">
  <svg class="abs" style="left:18px;top:18px" width="40" height="40" viewBox="0 0 40 40"><circle cx="16" cy="16" r="11" fill="none" stroke="#7a7a7a" stroke-width="4"/><line x1="24" y1="24" x2="36" y2="36" stroke="#7a7a7a" stroke-width="5" stroke-linecap="round"/></svg>
  <div class="field" style="left:79px;width:236px">What are you looking for?</div>
  <div class="field" style="left:325px;width:129px">Near Where?</div>
  <div class="go">GO</div>
</form>
<aside class="listing-card abs">
  <h3>Create A Directory<br>Listing Today</h3>
  <div class="listing-inner">
    <div class="cat">3 CATEGORY LISTING</div>
    <p>Promote Your Special Offers Business Profile &amp; Logo Website &amp; Email Link</p>
    <div class="go">GO</div>
  </div>
  <div class="price-band">A $ 25 PER YEAR</div>
  <span class="arrow" style="left:6px;top:180px">‹</span>
  <span class="arrow" style="left:252px;top:180px">›</span>
</aside>

<nav class="cat-bar abs">
  <span><i></i>BANKING</span><span><i></i>FINANCE &amp; INSURANCE</span><span><i></i>MARKETING</span><span><i></i>DESIGN</span><span><i></i>PHOTOGRAPHY</span><span><i></i>VIDEO &amp; PRINT</span><span><i></i>COACHING &amp; TRAINING</span><span><i></i>TECHNOLOGY</span>
</nav>

<!-- community -->
<section class="section-light abs" style="top:729px;height:645px"></section>
<h2 class="section-title abs" style="top:783px;font-weight:400">Get Real Support from Our Community</h2>
<p class="section-copy abs" style="top:844px">Lorem ipsum dolor sit amet, consectetur adipiscing elit, sed do eiusmod tempor incididunt ut labore et dolore magna aliqua. Ut enim ad minim veniam, quis nostrud exercitation ullamco laboris nisi ut aliquip ex ea commodo consequat.</p>
<div class="band abs" style="top:991px;height:64px"></div>

<div class="media" style="left:111px;top:932px;width:317px;height:186px;background:linear-gradient(135deg,#dfe6ee,#8ea3bd 60%,#50627c)" role="img" aria-label="Hands working on financial papers with a calculator"></div>
<div class="media" style="left:441px;top:932px;width:319px;height:186px;background:linear-gradient(135deg,#6b5548,#3a302b 60%,#241d19)" role="img" aria-label="Video still of a business audience"></div>
<svg class="abs" style="left:567px;top:992px" width="66" height="66" viewBox="0 0 66 66"><circle cx="33" cy="33" r="32" fill="rgba(255,255,255,.55)"/><path d="M26 20 L48 33 L26 46 Z" fill="#f29a1e"/></svg>
<div class="media partner" style="left:774px;top:932px;width:316px;height:186px"><span class="nav" style="left:12px">‹</span><span class="dot"></span>Parcelmint<span class="nav" style="right:12px">›</span></div>

<div class="abs" style="left:111px;top:1141px;width:317px">
  <div class="card-title">How Did You Sort Your Business</div>
  <p class="card-copy" style="margin-top:8px">Learn from Dana Morrow, a real small business owner. How she started her business and what are the most valuable resources for her right now.</p>
  <a class="read-more" style="display:block;margin-top:4px">READ MORE</a>
</div>
<div class="abs" style="left:441px;top:1141px;width:319px">
  <div class="card-title">Why Go with Tallyroo Link?</div>
  <p class="card-copy" style="margin-top:8px">What small business owner can't relate to the ongoing task of attracting new customers? Struggling with cash flow?</p>
  <a class="read-more" style="display:block;margin-top:4px">READ MORE</a>
</div>
<div class="abs" style="left:774px;top:1141px;width:316px">
  <div class="card-title">Become an Affiliate</div>
  <p class="card-copy" style="margin-top:8px">If you have a network of small businesses, let us help to create additional value for your members and make money for your network.</p>
  <a class="read-more" style="display:block;margin-top:4px">READ MORE</a>
</div>
<div class="offer-tab abs">Sign up for Daily Deals &nbsp;|&nbsp; Submit an Offer</div>

<!-- directory -->
<section class="section-dark abs"></section>
<h2 class="section-title dark-title abs" style="top:1441px;font-weight:400">Australia's Small Business Directory</h2>
<p class="dark-sub abs">Free Directory Listing, Business Solutions, Business Resources</p>
<div class="abs" style="left:111px;top:1573px;width:479px;height:221px;border-radius:6px;background:linear-gradient(180deg,#3a3a3a,#1e1e1e)" role="img" aria-label="Desktop, tablet and phone screens showing the directory homepage"></div>

<div class="block abs" style="left:639px;top:1605px;width:420px">
  <h4>ADVERTISE YOUR BUSINESS:</h4>
  <p>Do you sell a product or service? Want to reach Australian Small Business? It's simple and affordable.<br>Starting from just <span class="hl">$2</span> per day.</p>
  <p style="margin-top:10px">Contact Us To <span class="hl" style="text-decoration:underline">Get Started</span></p>
  <span class="btn" style="margin-top:10px">ADVERTISE NOW</span>
</div>
<div class="block abs" style="left:111px;top:1830px;width:420px">
  <h4>JOIN US:</h4>
  <p>We actively promote members with our daily deals, resource centre, newsletter and advertising.</p>
  <span class="btn" style="margin-top:14px">JOIN FREE</span>
</div>
<div class="block abs" style="left:639px;top:1830px;width:420px">
  <h4>SUBMIT AN OFFER:</h4>
  <p>Our directory gives members more purchasing choice and selling reach.</p>
  <span class="btn" style="margin-top:14px">SUBMIT OFFER</span>
</div>

<!-- get real support -->
<section class="section-light abs" style="top:2022px;height:612px;background:#f1f1f1"></section>
<h2 class="section-title abs" style="top:2076px;font-weight:400">Get Real Support</h2>
<p class="section-copy abs" style="top:2141px">Lorem ipsum dolor sit amet, consectetur adipiscing elit, sed do eiusmod tempor incididunt ut labore et dolore magna aliqua. Ut enim ad minim veniam, quis nostrud exercitation ullamco laboris nisi ut aliquip ex ea commodo consequat.</p>
<div class="band abs" style="top:2308px;height:62px"></div>
<span class="abs" style="left:138px;top:2315px;color:#999;font-size:32px;font-family:Questrial,sans-serif">‹</span>
<span class="abs" style="left:537px;top:2315px;color:#999;font-size:32px;font-family:Questrial,sans-serif">›</span>
<div class="media" style="left:191px;top:2241px;width:317px;height:194px;background:linear-gradient(135deg,#c85a4a,#5d7fb8 55%,#3d5a8c)" role="img" aria-label="Group of young people talking in a circle"></div>
<div class="media partner" style="left:723px;top:2241px;width:317px;height:194px"><span class="nav" style="left:14px">‹</span><span class="dot"></span>Parcelmint<span class="nav" style="right:14px">›</span></div>

<div class="abs" style="left:191px;top:2447px;width:320px">
  <div class="card-title">From The Vault</div>
  <p class="card-copy" style="margin-top:8px">What is leadership? How does poor ledership affect business?<br>Start of blog post or resource post to get them intrested in reading...</p>
  <a class="read-more" style="display:block;margin-top:4px">READ MORE</a>
</div>
<div class="abs" style="left:723px;top:2447px;width:320px">
  <div class="card-title">Affiliate ABC Brand</div>
  <p class="card-copy" style="margin-top:8px">We are collaborating wuith networking groups arround the country to bring our members more support and greater choice..</p>
  <a class="read-more" style="display:block;margin-top:4px">READ MORE</a>
</div>

<!-- footer -->
<footer class="site-footer abs">
  <div class="foot-col abs" style="left:111px;top:30px">
    <h5>SITE DIRECTORY:</h5>
    <ul><li>Search the Directory</li><li>Create a Directory Listing</li><li>Quote Finder</li><li>Coupns</li><li>Submit A coupons</li><li>Advertise With Us</li></ul>
  </div>
  <div class="foot-col abs" style="left:301px;top:30px">
    <h5>RESOURCES:</h5>
    <ul><li>Jointhe Forum</li><li>Submit an Article or Video</li><li>Affiliates</li><li>Become an Affiliate</li><li>Case Studies</li><li>Help Guides</li></ul>
  </div>
  <div class="foot-col abs" style="left:492px;top:30px">
    <h5>POPULAR CATEGORIES:</h5>
    <ul><li>Lorem ipsum dolor</li><li>Sit amet consec</li><li>Tetur adipiscing elit</li><li>Sed do euismod</li><li>Tempor incidunt</li><li>Magna aliqua</li></ul>
  </div>
  <div class="foot-col abs" style="left:703px;top:30px">
    <h5>ABOUT:</h5>
    <ul><li>About Us</li><li>Contact Us</li><li>Terms &amp; Conditions</li><li>Privacy Policy</li><li>Supporting City Councils</li><li>Site Map</li></ul>
  </div>
  <div class="foot-col abs" style="left:887px;top:30px">
    <h5>FOLLOW US:</h5>
    <div class="social-foot">
      <span class="sq" style="background:#3b5998"></span>
      <span class="sq" style="background:#d8332a"></span>
      <span class="sq" style="background:#1da1f2"></span>
      <span class="sq" style="background:#dd4b39"></span>
      <span class="sq" style="background:#0077b5"></span>
    </div>
    <span class="btn" style="margin-top:18px;width:203px;text-align:center;padding:0">SUBCRIBE COUPON DEALS</span>
  </div>
</footer>
<div class="bottom-bar abs">Copyrights © 2014 TallyrooLink.com - All Rights Reserved</div>

</body>
</html>
```